make a fireworks website

we are manufacturer of fireworks in Asia.
we need a HD fireworks website for showing product to all world customers.
we also need an register for member system,location, forum,products..etc
I added my Logo for the company.
brightnova.com.hk

and please message me if you have
any question.
here some example of website:
http://www.skyplumeshow.com/
http://www.tornelupyro.com/
http://www.quarvel-pyro.co.uk/
http://www.mirethpyro.co.uk/

```html
<!DOCTYPE html>
<html lang="en">
<head>
<meta charset="utf-8">
<title>BrightNova Fireworks</title>
<link href="https://fonts.googleapis.com/css2?family=Oswald:wght@400;600;700&family=Open+Sans:wght@400;600;700&display=swap" rel="stylesheet">
<style>
:root{
  --night:#07060f;
  --purple:#5e2a86;
  --purple-dark:#3f1a5e;
  --orange:#f6a31b;
  --pink:#d3186c;
  --pink-light:#ec3f8e;
  --red:#c4132f;
  --ink:#3a3a3a;
  --muted:#777;
  --panel:#ffffff;
  --grey:#eeeeee;
  --footer:#141414;
}
*{box-sizing:border-box;margin:0;padding:0}
html,body{width:1200px;height:2364px;overflow:hidden}
body{position:relative;background:var(--night);font-family:"Open Sans",sans-serif;color:var(--ink);font-size:12px;line-height:1.45}
.backdrop{position:absolute;inset:0;
  background:
   radial-gradient(ellipse 380px 260px at 600px 250px,rgba(230,60,140,.55),transparent 70%),
   radial-gradient(ellipse 260px 200px at 200px 330px,rgba(120,70,220,.45),transparent 70%),
   radial-gradient(ellipse 280px 200px at 1000px 300px,rgba(240,120,60,.4),transparent 70%),
   radial-gradient(ellipse 180px 260px at 60px 1500px,rgba(220,180,60,.35),transparent 70%),
   radial-gradient(ellipse 180px 260px at 1140px 1450px,rgba(230,80,160,.4),transparent 70%),
   radial-gradient(ellipse 300px 200px at 250px 2260px,rgba(240,180,60,.45),transparent 70%),
   radial-gradient(ellipse 300px 200px at 900px 2250px,rgba(230,70,150,.45),transparent 70%),
   linear-gradient(#1a1030 0,#2b1740 380px,#0a0814 560px,#05040a 100%);}
.header-top{position:absolute;top:12px;right:28px;display:flex;gap:18px;font-size:11px;color:#fff;font-weight:600}
.header-top span::before{content:"";display:inline-block;width:8px;height:8px;border-radius:50%;background:#fff;margin-right:6px;vertical-align:middle}
.logo{position:absolute;left:128px;top:76px;display:flex;align-items:center;gap:10px;color:#fff;font-family:"Oswald",sans-serif;font-weight:600;font-size:25px;line-height:1;white-space:nowrap}
.logo i{width:36px;height:36px;border-radius:50%;background:var(--pink);display:block;flex:none}
.main-nav{position:absolute;left:440px;top:72px;width:732px;height:48px;background:var(--purple);display:flex;align-items:center;border-radius:3px}
.main-nav a{color:#fff;text-decoration:none;font-family:"Oswald",sans-serif;font-size:15px;padding:0 21px;height:48px;line-height:48px}
.main-nav a.active{background:var(--orange)}
.hero-title{position:absolute;top:238px;left:0;width:1200px;text-align:center;font-family:"Oswald",sans-serif;font-weight:700;font-size:52px;color:var(--pink-light);letter-spacing:1px}
.buy-now{position:absolute;left:472px;top:420px;width:248px;height:50px;background:var(--pink);color:#fff;border-radius:4px;text-align:center;font-family:"Oswald",sans-serif;font-weight:600;font-size:26px;line-height:50px}
.slider-dots{position:absolute;top:494px;left:570px;display:flex;gap:10px}
.slider-dots b{width:10px;height:10px;border-radius:50%;background:rgba(255,255,255,.5)}
.slider-dots b:first-child{background:#fff}
.panel{position:absolute;left:128px;top:512px;width:944px;height:1546px;background:var(--panel);border-radius:4px}
.sec-title{font-family:"Oswald",sans-serif;font-weight:700;font-size:24px;color:var(--red);position:absolute}
.sec-title.pink{color:var(--pink);font-weight:400}
.view-all{position:absolute;right:24px;top:34px;color:var(--red);font-size:12px;text-decoration:underline}
.product-band{position:absolute;left:0;top:72px;width:944px;height:264px;background:var(--orange);display:flex;justify-content:space-around;align-items:center;padding:0 20px}
.product-card{width:196px;height:224px;background:#fff;border-radius:3px;padding:10px;text-align:center}
.product-card .shot{height:168px;border-radius:2px}
.product-card p{font-family:"Oswald",sans-serif;font-size:14px;margin-top:12px;color:#222}
.about{position:absolute;left:32px;top:380px;width:420px}
.about p{margin-top:46px;color:var(--muted);font-size:11.5px}
.about p+p{margin-top:10px}
.testimonials{position:absolute;left:484px;top:380px;width:428px}
.quote{margin-top:52px;background:var(--purple);color:#fff;border-radius:8px;padding:14px 18px;font-size:11.5px;position:relative}
.quote::after{content:"";position:absolute;right:60px;bottom:-14px;border:14px solid transparent;border-top-color:var(--purple);border-bottom:0}
.quote-by{text-align:right;margin-top:22px;font-size:12px;color:var(--ink)}
.countdown{position:absolute;left:32px;top:688px;width:420px;height:128px;background:#1b1b1b;border-radius:4px;color:#fff;text-align:center;font-family:"Oswald",sans-serif}
.countdown .digits{font-size:64px;font-weight:600;letter-spacing:2px;line-height:96px}
.countdown .labels{display:flex;justify-content:space-around;font-size:11px;color:#aaa;padding:0 30px}
.new-year{position:absolute;left:484px;top:688px;width:428px;height:128px;border-radius:4px;background:linear-gradient(120deg,#1a0a22,#5a1b4a 50%,#2a1030)}
.offer-band{position:absolute;left:0;top:896px;width:944px;height:236px;background:var(--pink);display:flex;justify-content:space-around;align-items:center;padding:0 16px}
.offer-card{width:204px;color:#fff;text-align:center}
.offer-card .shot{height:148px;background:#fff;border-radius:2px;padding:6px}
.offer-card .shot div{height:100%}
.offer-card p{font-size:11px;margin-top:8px;font-weight:600}
.col{position:absolute;top:1150px;width:280px}
.blog-item{display:flex;gap:10px;margin-top:12px}
.blog-item .thumb{width:66px;height:56px;flex:none;border-radius:2px;background:linear-gradient(135deg,#2a1540,#c23a6e)}
.blog-item b{display:block;font-size:11px;line-height:1.3}
.blog-item small{display:block;font-size:10px;color:var(--muted);line-height:1.35}
.blog-item a{color:var(--red);font-size:10px;line-height:1.35;display:block}
.tweet{display:flex;gap:10px;margin-top:16px;font-size:11px;color:var(--muted)}
.tweet i{width:14px;height:14px;border-radius:50%;background:#3fa9e0;flex:none;margin-top:2px}
.tweet a{color:#2a7cc0;display:block}
.contact-list{margin-top:18px;list-style:none;font-size:11px;color:var(--muted)}
.contact-list li{display:flex;gap:8px;align-items:center;margin-bottom:10px}
.socials{display:flex;gap:8px;margin-top:8px}
.socials b{width:26px;height:26px;border-radius:50%}
.secure{position:absolute;left:0;top:1448px;width:944px;height:98px;background:var(--grey);border-radius:0 0 4px 4px;padding:16px 24px}
.secure h4{font-size:12px;color:var(--red);font-weight:700}
.cards{display:flex;gap:10px;margin-top:14px}
.cards span{height:38px;padding:0 10px;border-radius:3px;background:#fff;border:1px solid #ccc;font-size:13px;font-weight:700;color:#26418a;line-height:36px}
.signup{position:absolute;right:24px;top:16px;width:300px}
.signup h4{text-align:right}
.signup .row{display:flex;margin-top:16px}
.signup .row span{flex:1;height:34px;background:#fff;border:1px solid #ccc;font-size:10px;color:#999;line-height:32px;padding-left:10px}
.signup .row b{background:var(--pink);color:#fff;font-size:12px;line-height:34px;padding:0 14px}
.footer{position:absolute;left:128px;top:2064px;width:944px;height:34px;background:var(--footer);color:#aaa;font-size:10px;display:flex;justify-content:space-between;align-items:center;padding:0 20px}
</style>
</head>
<body>
<div class="backdrop" role="img" aria-label="Night city harbour skyline with colourful fireworks bursting over the water"></div>

<div class="header-top"><span>REGISTER</span><span>LOGIN</span></div>
<div class="logo"><i></i>brightnova.com.hk</div>
<nav class="main-nav">
  <a class="active">HOME</a><a>LOCATIONS</a><a>OUR PRODUCTS</a><a>OFFERS</a><a>ABOUT</a><a>FORUM</a><a>CONTACT US</a>
</nav>
<h1 class="hero-title">WE MAKE YOUR DAYS MEMORABLE!</h1>
<div class="buy-now">BUY NOW!</div>
<div class="slider-dots"><b></b><b></b><b></b><b></b></div>

<main class="panel">
  <h2 class="sec-title" style="left:24px;top:24px">OUR PRODUCTS</h2>
  <a class="view-all">View all products</a>
  <div class="product-band">
    <div class="product-card"><div class="shot" role="img" aria-label="Fountain fireworks product" style="background:linear-gradient(#7fc3e8,#f0c8e0)"></div><p>FOUNTAINS</p></div>
    <div class="product-card"><div class="shot" role="img" aria-label="Display kit fireworks product" style="background:linear-gradient(#e8d06a,#c0392b)"></div><p>DISPLAY KITS</p></div>
    <div class="product-card"><div class="shot" role="img" aria-label="Pan barrage fireworks box" style="background:linear-gradient(#3b4a8a,#d95a3a)"></div><p>PAN BARRAGES</p></div>
    <div class="product-card"><div class="shot" role="img" aria-label="Rocket fireworks product" style="background:linear-gradient(#d83a3a,#e8a04a)"></div><p>ROCKETS</p></div>
  </div>

  <section class="about">
    <h2 class="sec-title pink" style="left:0;top:0">ABOUT US</h2>
    <p>Lorem ipsum dolor sit amet, consectetur adipiscing elit. Aliquam in ante nec ipsum vehicula interdum. Mauris hendrerit quis dolor nec fringilla. Etiam lobortis justo eu nunc molestie, a fringilla ipsum pellentesque.</p>
    <p>Duis adipiscing odio rhoncus auctor viverra. Pellentesque luctus nibh consectetur ut semper. Nunc pretium eget tempor. In aliquam suscipit volutpat. Proin cursus mauris massa, ac consectetur tortor egestas a. Curabitur tempor convallis felis, id varius risus ullamcorper non. Nam faucibus dui sit amet tellus dictum, vitae eleifend orci tincidunt. Duis augue leo, non ultricies nibh dapibus at. Vivamus fringilla varius enim vitae dapibus tortor.</p>
  </section>

  <section class="testimonials">
    <h2 class="sec-title pink" style="left:0;top:0">TESTIMONIALS</h2>
    <div class="quote">Lorem ipsum dolor sit amet, consectetur adipiscing elit. Aliquam in ante nec ipsum vehicula interdum. Mauris hendrerit quis dolor nec fringilla. Etiam lobortis justo eu nunc molestie, a fringilla ipsum pellentesque. Duis adipiscing odio rhoncus auctor viverra.</div>
    <p class="quote-by">Rory K, Hong Kong</p>
  </section>

  <div class="countdown">
    <div class="digits">04.23.38.06</div>
    <div class="labels"><span>DAYS</span><span>HOURS</span><span>MINUTES</span><span>SECONDS</span></div>
  </div>
  <div class="new-year" role="img" aria-label="New Year coming soon banner with fireworks"></div>

  <h2 class="sec-title" style="left:24px;top:852px">SPECIAL OFFERS</h2>
  <div class="offer-band">
    <div class="offer-card"><div class="shot"><div role="img" aria-label="Candle battery firework" style="background:linear-gradient(#6fd07a,#2a8a4a)"></div></div><p>$4.25 each 8MT CANDLE BATTERY</p></div>
    <div class="offer-card"><div class="shot"><div role="img" aria-label="Barrage pack box" style="background:linear-gradient(#e0b030,#c02a2a)"></div></div><p>$100.00 was $130.00<br>BONFIRE BARRAGE PACK</p></div>
    <div class="offer-card"><div class="shot"><div role="img" aria-label="Festival display fireworks" style="background:linear-gradient(#1a1a40,#b02a8a)"></div></div><p>$150.00 was $180.00<br>BIG FESTIVAL DISPLAY</p></div>
    <div class="offer-card"><div class="shot"><div role="img" aria-label="Thunder cake box" style="background:linear-gradient(#8a5a3a,#3a2a1a)"></div></div><p>$160.00 was $190.00<br>CLOUD OF THUNDER CAKE</p></div>
  </div>

  <section class="col" style="left:24px">
    <h2 class="sec-title" style="position:static">RECENT BLOGS</h2>
    <div class="blog-item"><div class="thumb" role="img" aria-label="Fireworks display blog thumbnail"></div><div><small>June 14th, 2014</small><b>Fireworks displays</b><small>Lorem ipsum dolor sit amet...</small><a>Read more</a></div></div>
    <div class="blog-item"><div class="thumb" role="img" aria-label="Fireworks display blog thumbnail"></div><div><small>June 14th, 2014</small><b>Fireworks displays</b><small>Lorem ipsum dolor sit amet...</small><a>Read more</a></div></div>
    <div class="blog-item"><div class="thumb" role="img" aria-label="Fireworks display blog thumbnail"></div><div><small>June 14th, 2014</small><b>Fireworks displays</b><small>Lorem ipsum dolor sit amet...</small><a>Read more</a></div></div>
  </section>

  <section class="col" style="left:334px">
    <h2 class="sec-title" style="position:static">LATEST TWEETS</h2>
    <div class="tweet"><i></i><div>Lorem ipsum dolor sit amet, consectetur adipiscing.<a>http://brn.hk/x4Tq2</a>1 day ago</div></div>
    <div class="tweet"><i></i><div>Lorem ipsum dolor sit amet, consectetur adipiscing.<a>http://brn.hk/x4Tq2</a>1 day ago</div></div>
    <div class="tweet"><i></i><div>Lorem ipsum dolor sit amet, consectetur adipiscing.<a>http://brn.hk/x4Tq2</a>1 day ago</div></div>
  </section>

  <section class="col" style="left:640px">
    <h2 class="sec-title" style="position:static">CONTACT US</h2>
    <ul class="contact-list">
      <li><svg width="12" height="14" viewBox="0 0 12 14"><path d="M6 0a5 5 0 0 1 5 5c0 4-5 9-5 9S1 9 1 5a5 5 0 0 1 5-5z" fill="#c4132f"/><circle cx="6" cy="5" r="2" fill="#fff"/></svg><span>brightnova.com.hk<br>208 Harbour Drive, Kowloon, Hong Kong</span></li>
      <li><svg width="12" height="12" viewBox="0 0 12 12"><path d="M2 0h3l1 3-2 1a7 7 0 0 0 4 4l1-2 3 1v3c0 1-1 2-2 2C5 12 0 7 0 2 0 1 1 0 2 0z" fill="#c4132f"/></svg>852-424-2250</li>
      <li><svg width="14" height="10" viewBox="0 0 14 10"><rect width="14" height="10" fill="#c4132f"/><path d="M0 0l7 6 7-6" fill="none" stroke="#fff"/></svg>info@brightnova.com.hk</li>
    </ul>
    <div class="socials"><b style="background:#3b5998"></b><b style="background:#3fa9e0"></b><b style="background:#dd4b39"></b><b style="background:#0e76a8"></b><b style="background:#cb2027"></b></div>
  </section>

  <div class="secure">
    <h4>Secure Purchasing - We accept the following methods of payment</h4>
    <div class="cards"><span>Cardlane</span><span>Tessro</span><span>Veyra</span><span>Ambrel</span><span>PayWisp</span></div>
    <div class="signup"><h4>Signup for our deals and Special offers</h4><div class="row"><span>Enter email here</span><b>SIGNUP</b></div></div>
  </div>
</main>

<footer class="footer"><span>HOME | LOCATIONS | OUR PRODUCTS | OFFERS | ABOUT | FORUM | CONTACT US</span><span>© COPYRIGHT 2014 BRIGHTNOVA.COM.HK</span></footer>
</body>
</html>
```